Plumerly Ad for “7 Step Signature Presence Sprint”

I would like a Plumerly ad graphic for this offer:
https://www.morvindeals.net/7-step-signature-presence-sprint
Please include my photo- I have attached images to use (remove the background)
The big selling points are the three focus points during the challenge (Plumerly Page, Taskvane profile and the web site) and the cost is only $5.40
I will choose the winner who submits one ad, and then the winner will be asked to provide two variations of the ad graphic so I can test all three graphics.
Thank you, I’m looking forward to seeing your ideas and designs!

```html
<!DOCTYPE html>
<html lang="en">
<head>
<meta charset="utf-8">
<title>7 Step Signature Presence Sprint – Plumerly Ad</title>
<link rel="stylesheet" href="https://fonts.googleapis.com/css2?family=Open+Sans:wght@600;700;800&display=swap">
<style>
  :root {
    --brand-blue: #2d5b99;
    --band-blue: #2a5796;
    --band-line: #4a7bc0;
    --teal: #34c3c8;
    --navy: #1d2a6e;
    --badge-light: #4f86c9;
    --badge-dark: #2a4f96;
    --ring: #4a86c2;
    --ink: #1b1b1b;
    --white: #ffffff;
    --photo-top: #3b4f66;
    --photo-bottom: #2f4f86;
  }
  * { margin: 0; padding: 0; box-sizing: border-box; }
  html, body { width: 1200px; height: 1200px; overflow: hidden; background: var(--white); }
  body { font-family: "Open Sans", Arial, sans-serif; }

  .ad { position: relative; width: 1200px; height: 1200px; background: var(--white); overflow: hidden; }

  .ad__backdrop { position: absolute; inset: 0; width: 1200px; height: 1200px; }

  .brand {
    position: absolute; top: 42px; left: 0; width: 1200px;
    display: flex; justify-content: center; align-items: center; gap: 16px;
    color: var(--white); font-weight: 700; font-size: 38px; letter-spacing: 0.5px;
  }
  .brand__dot { width: 40px; height: 40px; border-radius: 50%; background: var(--white); }

  .headline {
    position: absolute; top: 158px; left: 0; width: 1200px; text-align: center;
    font-weight: 800; text-transform: uppercase; line-height: 1;
  }
  .headline__accent { display: block; color: var(--teal); font-size: 70px; }
  .headline__middle { display: block; color: var(--white); font-size: 42px; font-weight: 700; margin: 14px 0 12px; }

  .price-badge {
    position: absolute; left: 56px; top: 367px; width: 212px; height: 212px; border-radius: 50%;
    background: radial-gradient(circle at 45% 40%, var(--badge-light), var(--badge-dark));
    border: 7px solid var(--navy);
    display: flex; flex-direction: column; justify-content: center; align-items: center;
    color: var(--white); font-weight: 800; line-height: 1;
  }
  .price-badge__label { font-size: 50px; }
  .price-badge__amount { font-size: 48px; margin-top: 4px; }

  .copy {
    position: absolute; left: 55px; width: 512px;
    border-left: 3px solid var(--brand-blue); padding-left: 12px;
    color: var(--ink); font-weight: 600; font-size: 22.5px; line-height: 38px;
    text-transform: uppercase; text-align: justify;
  }
  .copy--offer { top: 602px; }
  .copy--plan { top: 812px; }

  .cta {
    position: absolute; left: 177px; top: 1034px; width: 256px; height: 52px;
    border-radius: 14px; background: var(--navy); border: 3px solid var(--ring);
    color: var(--white); font-weight: 700; font-size: 24px;
    display: flex; justify-content: center; align-items: center;
  }

  .photo {
    position: absolute; left: 700px; top: 352px; width: 480px; height: 848px;
    border-radius: 220px 220px 0 0;
    background: linear-gradient(180deg, var(--photo-top), var(--photo-bottom));
  }

  .footer-band {
    position: absolute; left: 0; top: 1108px; width: 1200px; height: 92px;
    background: var(--band-blue); border-top: 6px solid var(--band-line);
    display: flex; align-items: center; padding-left: 423px;
    color: var(--white); font-weight: 600; font-size: 25px;
  }
</style>
</head>
<body>
<main class="ad">
  <svg class="ad__backdrop" viewBox="0 0 1200 1200" aria-hidden="true">
    <path d="M0 0 H1200 V132 C1200 330 900 452 600 452 C300 452 0 330 0 132 Z" fill="var(--brand-blue)"/>
    <g fill="#8fb0dc">
      <g class="dot-grid dot-grid--left">
        <circle cx="62" cy="25" r="2.4"/><circle cx="74" cy="25" r="2.4"/><circle cx="86" cy="25" r="2.4"/><circle cx="98" cy="25" r="2.4"/><circle cx="110" cy="25" r="2.4"/><circle cx="122" cy="25" r="2.4"/>
        <circle cx="62" cy="41" r="2.4"/><circle cx="74" cy="41" r="2.4"/><circle cx="86" cy="41" r="2.4"/><circle cx="98" cy="41" r="2.4"/><circle cx="110" cy="41" r="2.4"/><circle cx="122" cy="41" r="2.4"/>
        <circle cx="62" cy="57" r="2.4"/><circle cx="74" cy="57" r="2.4"/><circle cx="86" cy="57" r="2.4"/><circle cx="98" cy="57" r="2.4"/><circle cx="110" cy="57" r="2.4"/><circle cx="122" cy="57" r="2.4"/>
        <circle cx="62" cy="73" r="2.4"/><circle cx="74" cy="73" r="2.4"/><circle cx="86" cy="73" r="2.4"/><circle cx="98" cy="73" r="2.4"/><circle cx="110" cy="73" r="2.4"/><circle cx="122" cy="73" r="2.4"/>
      </g>
      <g class="dot-grid dot-grid--right">
        <circle cx="1066" cy="25" r="2.4"/><circle cx="1078" cy="25" r="2.4"/><circle cx="1090" cy="25" r="2.4"/><circle cx="1102" cy="25" r="2.4"/><circle cx="1114" cy="25" r="2.4"/><circle cx="1126" cy="25" r="2.4"/>
        <circle cx="1066" cy="41" r="2.4"/><circle cx="1078" cy="41" r="2.4"/><circle cx="1090" cy="41" r="2.4"/><circle cx="1102" cy="41" r="2.4"/><circle cx="1114" cy="41" r="2.4"/><circle cx="1126" cy="41" r="2.4"/>
        <circle cx="1066" cy="57" r="2.4"/><circle cx="1078" cy="57" r="2.4"/><circle cx="1090" cy="57" r="2.4"/><circle cx="1102" cy="57" r="2.4"/><circle cx="1114" cy="57" r="2.4"/><circle cx="1126" cy="57" r="2.4"/>
        <circle cx="1066" cy="73" r="2.4"/><circle cx="1078" cy="73" r="2.4"/><circle cx="1090" cy="73" r="2.4"/><circle cx="1102" cy="73" r="2.4"/><circle cx="1114" cy="73" r="2.4"/><circle cx="1126" cy="73" r="2.4"/>
      </g>
    </g>
    <g class="floating-rings" fill="none" stroke="var(--ring)" stroke-width="2.5">
      <circle cx="235" cy="106" r="8"/><circle cx="162" cy="176" r="8"/><circle cx="219" cy="268" r="8"/>
      <circle cx="861" cy="136" r="8"/><circle cx="967" cy="176" r="8"/><circle cx="958" cy="268" r="8"/>
      <circle cx="371" cy="494" r="8"/><circle cx="711" cy="503" r="8"/>
    </g>
  </svg>

  <div class="brand"><span class="brand__dot"></span><span class="brand__name">KESTREL GROUP</span></div>

  <h1 class="headline">
    <span class="headline__accent">7 Step</span>
    <span class="headline__middle">Signature Presence</span>
    <span class="headline__accent">Sprint!</span>
  </h1>

  <div class="price-badge">
    <span class="price-badge__label">ONLY</span>
    <span class="price-badge__amount">5.40</span>
  </div>

  <p class="copy copy--offer">For only $5.40 (the exact price of my favorite Brewhaven drink) you get my quick action, take-me-by-the-hands guide to get your personal online presence set up.</p>

  <p class="copy copy--plan">When you join my brand new "7 Step Signature Presence Action Plan" you’re working with me, in bite-size steps, to get your online presence built out and ready for growth!</p>

  <div class="cta">GET START NOW!</div>

  <div class="photo" role="img" aria-label="Cut-out photo of the host sitting on a wooden bar stool in a dark T-shirt, jeans and blue sneakers"></div>

  <footer class="footer-band">www.morvindeals.net</footer>
</main>
</body>
</html>
```